We manage actors careers and book them liaising and promoting their profiles internationally through Casting Directors, Producers, Directors, Publicists etc. We need clearly visable contact details but with a design that reflects our status and creativity of TV, Feature Film industry. Our logo is attached and needs to relate and our website is www.brovanelpartners.example
No flame designs please but please incorporate logo colours.

Target Market(s)

Clients

Industry/Entity Type

Film Production

Contact Information for Business Card

Director Danielle Pacrow
Suite F, Building 7, Wren Lot Studios, Tallis Reach, Sydney, NSW 2094

Font styles to use
Sans Serif

Colors
ec1f27

Requirements
Nice to have
• Colours should relate to logo attached and type can relate again to type in the logo design.
Should not have
• No Flames designs and best to be not too obvious with the film designs eiither. Needs to be more creative and modern

```html
<!DOCTYPE html>
<html lang="en">
<head>
<meta charset="utf-8">
<title>Brovanel Partners – Business Card</title>
<link rel="stylesheet" href="https://fonts.googleapis.com/css2?family=Exo+2:wght@400;500;600;700&display=swap">
<style>
  :root {
    --brand-red: #ec1f27;
    --deep-red: #c41a22;
    --ink: #1b1b1b;
    --paper: #ffffff;
    --paper-shade: #eeeeee;
    --stage: #e4e1dc;
    --rule: #c9c9c9;
  }
  * { box-sizing: border-box; margin: 0; padding: 0; }
  html, body { width: 1200px; height: 885px; overflow: hidden; }
  body {
    background: var(--stage);
    font-family: "Exo 2", sans-serif;
    position: relative;
  }
  .card {
    position: absolute;
    left: 260px;
    width: 680px;
    height: 389px;
    border-radius: 18px;
    overflow: hidden;
    box-shadow: 0 10px 26px rgba(0,0,0,0.22);
  }
  .card-front { top: 36px; background: linear-gradient(160deg, var(--paper) 0%, var(--paper-shade) 100%); }
  .card-back { top: 460px; background: linear-gradient(160deg, #e52a31 0%, var(--deep-red) 100%); }

  .front-wave { position: absolute; inset: 0; width: 100%; height: 100%; }

  .front-brand {
    position: absolute;
    left: 48px;
    top: 250px;
    font-weight: 700;
    font-size: 30px;
    letter-spacing: 1px;
    color: var(--brand-red);
  }
  .front-divider {
    position: absolute;
    left: 250px;
    top: 150px;
    width: 1px;
    height: 120px;
    background: var(--rule);
    transform: rotate(28deg);
  }
  .contact-block { position: absolute; left: 300px; top: 70px; }
  .person-name { font-size: 26px; font-weight: 600; color: var(--brand-red); line-height: 1.1; }
  .person-role { font-size: 21px; font-weight: 500; color: var(--ink); margin-top: 2px; }
  .contact-list { list-style: none; margin-top: 26px; }
  .contact-item {
    display: flex; align-items: center; gap: 10px;
    font-size: 15px; color: var(--ink); margin-bottom: 8px;
  }
  .contact-icon { width: 20px; height: 20px; flex: none; }

  .back-brand {
    position: absolute;
    left: 0; right: 0; top: 105px;
    text-align: center;
    font-weight: 700;
    font-size: 62px;
    letter-spacing: 3px;
    color: var(--paper);
  }
  .address-band {
    position: absolute;
    left: 0; right: 0; bottom: 44px;
    height: 40px;
    background: linear-gradient(90deg, #f4f4f4, #dcdcdc);
    display: flex; align-items: center; justify-content: center;
  }
  .address-text { font-size: 16px; font-weight: 500; color: var(--brand-red); }
</style>
</head>
<body>

  <section class="card card-front" aria-label="Business card front">
    <svg class="front-wave" viewBox="0 0 680 389" preserveAspectRatio="none" aria-hidden="true">
      <path d="M170,389 C400,372 560,300 604,170 C630,95 652,40 680,14 L680,389 Z" fill="#1b1b1b"/>
      <path d="M196,389 C420,376 572,306 616,180 C640,106 660,52 680,30 L680,389 Z" fill="#ec1f27"/>
      <path d="M196,389 C420,376 572,306 616,180 C640,106 660,52 680,30 L680,389 Z" fill="url(#waveShade)"/>
      <defs>
        <linearGradient id="waveShade" x1="0" y1="0" x2="1" y2="1">
          <stop offset="0" stop-color="#ffffff" stop-opacity="0.08"/>
          <stop offset="1" stop-color="#000000" stop-opacity="0.15"/>
        </linearGradient>
      </defs>
    </svg>

    <div class="front-brand">BROVANEL PARTNERS</div>
    <div class="front-divider"></div>

    <div class="contact-block">
      <p class="person-name">Danielle Pacrow</p>
      <p class="person-role">Director</p>
      <ul class="contact-list">
        <li class="contact-item">
          <svg class="contact-icon" viewBox="0 0 20 20" aria-hidden="true">
            <rect width="20" height="20" rx="4" fill="#ec1f27"/>
            <path d="M6 4.5l2.2 0.6-0.6 2.6 1.2 2 2 1.3 2.5-0.7 0.7 2.2c-1 1.4-2.6 1.8-4.3 0.9-2.2-1.2-4-3.2-4.9-5.5-0.6-1.5-0.2-2.6 1.2-3.4z" fill="#fff"/>
          </svg>
          +61 (0) 400 555 017
        </li>
        <li class="contact-item">
          <svg class="contact-icon" viewBox="0 0 20 20" aria-hidden="true">
            <rect width="20" height="20" rx="4" fill="#ec1f27"/>
            <rect x="4" y="6" width="12" height="8" fill="none" stroke="#fff" stroke-width="1.4"/>
            <path d="M4 6l6 5 6-5" fill="none" stroke="#fff" stroke-width="1.4"/>
          </svg>
          danielle@brovanelpartners.example
        </li>
        <li class="contact-item">
          <svg class="contact-icon" viewBox="0 0 20 20" aria-hidden="true">
            <rect width="20" height="20" rx="4" fill="#ec1f27"/>
            <circle cx="10" cy="10" r="5.5" fill="none" stroke="#fff" stroke-width="1.3"/>
            <ellipse cx="10" cy="10" rx="2.3" ry="5.5" fill="none" stroke="#fff" stroke-width="1.1"/>
            <path d="M4.5 10h11" stroke="#fff" stroke-width="1.1"/>
          </svg>
          www.brovanelpartners.example
        </li>
      </ul>
    </div>
  </section>

  <section class="card card-back" aria-label="Business card back">
    <div class="back-brand">BROVANEL PARTNERS</div>
    <div class="address-band">
      <p class="address-text">Wren Lot Studios, Tallis Reach, Sydney, NSW 2094</p>
    </div>
  </section>

</body>
</html>
```